TulipaMoonsXo947

I want to create a website that will have fun design. The subject is the crazy drivers in Miami. I want to show a cool logo, a top banner on the website that is a video background.

And then below I would like to have advertisements, and then a collection of video, article, and image divs shown that can be clicked on. Each page opened will have advertising or affiliate marketing links.

```html
<!DOCTYPE html>
<html lang="en">
<head>
<meta charset="utf-8">
<title>TulipaMoonsXo947 — Miami Streets</title>
<link rel="stylesheet" href="https://fonts.googleapis.com/css2?family=Inter+Tight:wght@400;500;600;700;800&family=Montserrat:wght@400;500;600&display=swap">
<style>
:root{
  --bg:#000000;
  --panel:#111111;
  --line:#262626;
  --pink:#ff8fab;
  --pink-deep:#e8769a;
  --cyan:#1ad4e8;
  --white:#ffffff;
}
*{box-sizing:border-box;margin:0;padding:0}
html,body{width:1200px;height:3346px;overflow:hidden;background:var(--bg);color:var(--white)}
body{position:relative;font-family:"Inter Tight",sans-serif}
.abs{position:absolute}
.caps{font-family:"Montserrat",sans-serif;text-transform:uppercase}

/* header */
.site-header{left:0;top:0;width:1200px;height:98px;border-bottom:1px solid var(--line);background:#050505}
.brand{left:26px;top:39px;display:flex;align-items:center;gap:7px;font-weight:700;font-size:14px;color:var(--pink);white-space:nowrap}
.brand-dot{width:10px;height:10px;border-radius:50%;background:var(--pink)}
.main-nav a{position:absolute;top:38px;font-size:15px;color:#cfcfcf;text-decoration:none;letter-spacing:-.2px}
.main-nav a.active{color:var(--pink);border-bottom:2px solid var(--pink);padding-bottom:6px}
.search{left:783px;top:29px;width:239px;height:39px;background:#1a1a1a;border:1px solid #2e2e2e;display:flex;align-items:center;padding-left:12px;gap:12px;font-size:12px;letter-spacing:2px;color:#777}
.btn-submit-top{left:1038px;top:29px;width:132px;height:39px;background:var(--pink);color:#111;font-size:13px;font-weight:600;display:flex;align-items:center;justify-content:center;letter-spacing:-.3px}

/* sidebar */
.sidebar{left:0;top:98px;width:269px;height:584px;border-right:1px solid #1c1c1c}
.feed-title{left:30px;top:141px;font-size:20px;font-weight:500;letter-spacing:-.5px}
.feed-live{left:30px;top:168px;font-size:13px;letter-spacing:2.5px;color:#bbb;display:flex;align-items:center;gap:7px}
.feed-live i{width:6px;height:6px;border-radius:50%;background:var(--pink);display:block}
.side-sep{left:0;top:214px;width:269px;height:1px;background:#1a1a1a}
.side-item{left:0;width:269px;height:57px;display:flex;align-items:center;gap:16px;padding-left:30px;font-size:13px;letter-spacing:2.5px;color:#9a9a9a}
.side-item.active{background:#121212;border-left:3px solid var(--pink);color:var(--cyan);padding-left:33px}
.side-item svg{width:18px;height:18px}
.btn-premium{left:30px;top:597px;width:221px;height:55px;border:2px solid var(--cyan);color:var(--cyan);font-size:13px;letter-spacing:2.5px;display:flex;align-items:center;justify-content:center}

/* hero */
.hero{left:269px;top:100px;width:931px;height:481px;background:linear-gradient(180deg,#3a4a5a 0%,#2a3a44 35%,#4a2f3c 62%,#1e1a20 100%)}
.hero::after{content:"";position:absolute;inset:0;background:linear-gradient(90deg,rgba(0,0,0,.55) 0%,rgba(0,0,0,.1) 70%)}
.hero-tag{left:331px;top:145px;height:22px;padding:0 9px;background:var(--pink-deep);font-size:11px;letter-spacing:2px;display:flex;align-items:center;color:#fff;z-index:2}
.hero-title{left:331px;top:208px;font-size:86px;line-height:88px;font-weight:800;letter-spacing:-4px;z-index:2;white-space:nowrap}
.hero-title span{display:block;color:var(--pink)}
.btn-watch{left:331px;top:439px;width:234px;height:66px;background:var(--pink);color:#111;font-size:19px;letter-spacing:-1px;display:flex;align-items:center;justify-content:center;z-index:2}
.btn-latest{left:581px;top:439px;width:220px;height:66px;border:2px solid #fff;color:#fff;font-size:19px;letter-spacing:-1px;display:flex;align-items:center;justify-content:center;z-index:2}

/* sponsored */
.sponsored{left:300px;top:620px;width:870px;height:119px;background:var(--panel);border:1px solid #2a2a2a;text-align:center}
.sponsored small{display:block;margin-top:30px;font-size:13px;letter-spacing:6px;color:#666}
.sponsored strong{display:block;margin-top:14px;font-size:27px;font-weight:400;letter-spacing:4px;color:#e8e8e8}

/* trending */
.trend-bar{left:331px;top:841px;width:59px;height:4px;background:var(--pink)}
.section-title{font-size:47px;font-weight:500;letter-spacing:-2.5px}
.trend-title{left:406px;top:818px}
.trend-sub{left:421px;top:874px;font-size:13px;letter-spacing:4.5px;color:#777}
.viewers{left:955px;top:857px;width:184px;height:31px;border:1px solid #2a3a3c;border-radius:16px;background:#0b1314;color:var(--cyan);font-size:13px;letter-spacing:1.5px;display:flex;align-items:center;justify-content:center;gap:10px}
.viewers i{width:8px;height:8px;border-radius:50%;background:var(--cyan);display:block}
.trend-rule{left:331px;top:912px;width:808px;height:1px;background:#2a2a2a}
.feature{top:951px;width:385px;height:217px;border:1px solid #1e1e1e}
.feature.one{left:331px;background:linear-gradient(180deg,#6a6a6a 0%,#3a3a3a 50%,#0d0d0d 100%)}
.feature.two{left:755px;background:linear-gradient(180deg,#8a8a8a 0%,#3c3c3c 45%,#0d0d0d 100%)}
.feature-tag{position:absolute;left:30px;top:88px;height:20px;padding:0 9px;font-size:11px;letter-spacing:2px;display:flex;align-items:center}
.feature.one .feature-tag{background:var(--pink-deep)}
.feature.two .feature-tag{background:var(--cyan);color:#06363c}
.feature h3{position:absolute;left:30px;top:112px;font-size:28px;line-height:34px;font-weight:600;letter-spacing:-1.6px;width:340px}

/* latest heat */
.latest-title{left:331px;top:1256px;font-size:35px;letter-spacing:-2px}
.latest-rule{left:540px;top:1276px;width:180px;height:1px;background:#333}
.clip-thumb{width:180px;height:180px;border:1px solid #2a2a2a}
.thumb-crash{background:radial-gradient(circle at 50% 55%,#7a7a7a 0%,#3a3a3a 40%,#151515 100%)}
.thumb-street{background:linear-gradient(180deg,#1d3442 0%,#2a5a70 55%,#0b1a22 100%)}
.thumb-night{background:radial-gradient(circle at 50% 50%,#1d4a6a 0%,#0f2a44 55%,#0a1a2c 100%)}
.clip-tag{position:absolute;height:19px;padding:0 10px;font-size:10px;letter-spacing:1.5px;display:flex;align-items:center}
.clip-tag.pink{background:var(--pink-deep);color:#fff}
.clip-tag.cyan{background:var(--cyan);color:#06363c}
.clip-title{font-size:15px;line-height:21px;letter-spacing:-.7px;color:#e8e8e8;width:165px}
.clip-title.narrow{width:150px}
.clip-meta{font-size:11px;color:#666;display:flex;gap:8px;align-items:center;white-space:nowrap}
.clip-meta .views{color:var(--pink)}
.clip-meta .views.cy{color:var(--cyan)}
.clip-meta i{width:3px;height:3px;border-radius:50%;background:#555;display:block}
.btn-more{left:331px;top:1987px;width:389px;height:59px;border:1px solid #444;display:flex;align-items:center;justify-content:center;font-size:13px;letter-spacing:5px;color:#bbb}

/* aside */
.topics{left:779px;top:1259px;width:360px;height:227px;background:var(--panel)}
.topics h4{position:absolute;left:31px;top:26px;font-size:21px;font-weight:500;letter-spacing:3px;color:var(--cyan)}
.hashtag{position:absolute;height:29px;padding:0 14px;background:#1c1c1c;font-size:11px;letter-spacing:1px;color:#bbb;display:flex;align-items:center;white-space:nowrap}
.ad-box{left:779px;top:1547px;width:360px;height:496px;background:var(--panel);border:1px solid #1e1e1e}
.ad-box .ad-label{position:absolute;top:32px;width:100%;text-align:center;font-size:13px;font-weight:600;letter-spacing:5px}
.ad-photo{position:absolute;left:62px;top:56px;width:238px;height:269px;background:linear-gradient(180deg,#e4e4e4 0%,#bdb6a8 55%,#5b4e38 100%)}
.ad-box .ad-line{position:absolute;top:350px;width:100%;text-align:center;font-size:14px;letter-spacing:4px;color:#ddd}
.btn-shop{position:absolute;left:32px;top:391px;width:297px;height:36px;background:#fff;color:#111;font-size:13px;font-weight:600;letter-spacing:2px;display:flex;align-items:center;justify-content:center}
.chatter-title{left:779px;top:2098px;font-size:21px;font-weight:400;letter-spacing:3px;color:var(--pink);font-family:"Montserrat",sans-serif}
.chatter-rule{left:779px;top:2137px;width:360px;height:1px;background:#3a1f28}
.comment{left:779px;width:360px;height:98px;background:var(--panel);padding:17px 20px 0 20px}
.comment.cy{border-left:2px solid var(--cyan)}
.comment.pk{border-left:2px solid var(--pink)}
.comment b{display:block;font-family:"Montserrat",sans-serif;font-weight:400;font-size:13px;letter-spacing:1.5px}
.comment.cy b{color:var(--cyan)}
.comment.pk b{color:var(--pink)}
.comment p{margin-top:8px;font-size:13px;line-height:19px;color:#ccc;width:300px}

/* call to action */
.cta-band{left:0;top:2817px;width:1200px;height:6px;background:var(--pink)}
.cta{left:331px;top:2433px;width:808px;height:386px;background:var(--pink);border-radius:16px;overflow:hidden}
.cta-stripes{position:absolute;left:30px;top:40px}
.cta h2{position:absolute;left:75px;top:88px;font-size:62px;line-height:74px;font-weight:800;letter-spacing:-4.5px;color:#111;white-space:nowrap}
.cta p{position:absolute;left:75px;top:265px;width:380px;font-size:22px;line-height:30px;letter-spacing:-1px;color:#3a1a22}
.btn-submit-cta{position:absolute;left:491px;top:152px;width:273px;height:92px;background:#000;color:var(--pink);font-size:29px;letter-spacing:-1.5px;display:flex;align-items:center;justify-content:center}

/* footer */
.foot-brand{left:0;top:2928px;width:1200px;display:flex;justify-content:center;align-items:center;gap:10px;font-size:28px;font-weight:700;color:var(--pink)}
.foot-brand i{width:16px;height:16px;border-radius:50%;background:var(--pink);display:block}
.foot-tag{left:0;top:3020px;width:1200px;text-align:center;font-size:13px;letter-spacing:5px;color:#ddd}
.foot-links{left:0;top:3080px;width:1200px;display:flex;justify-content:center;gap:44px;font-size:12px;letter-spacing:3px;color:#ccc}
.foot-icons{left:0;top:3152px;width:1200px;display:flex;justify-content:center;gap:30px}
.foot-icons svg{width:24px;height:24px}
.legal{left:0;top:3240px;width:1200px;text-align:center;font-size:12px;line-height:15px;letter-spacing:2.5px;color:#888}
</style>
</head>
<body>

<header class="abs site-header">
  <div class="abs brand"><span class="brand-dot"></span>TulipaMoonsXo947</div>
  <nav class="main-nav">
    <a class="active" style="left:190px">HOME</a>
    <a style="left:264px">VIDEOS</a>
    <a style="left:346px">ACCIDENTS</a>
    <a style="left:458px">ARTICLES</a>
    <a style="left:556px">ABOUT</a>
  </nav>
  <div class="abs search caps">
    <svg width="12" height="12" viewBox="0 0 12 12"><circle cx="5" cy="5" r="3.5" fill="none" stroke="#888" stroke-width="1.5"/><line x1="7.5" y1="7.5" x2="11" y2="11" stroke="#888" stroke-width="1.5"/></svg>
    Search chaos...
  </div>
  <div class="abs btn-submit-top">SUBMIT CLIP</div>
</header>

<aside class="abs sidebar"></aside>
<div class="abs feed-title">THE FEED</div>
<div class="abs feed-live caps"><i></i>305 Live Now</div>
<div class="abs side-sep"></div>
<div class="abs side-item active caps" style="top:238px">
  <svg viewBox="0 0 18 18"><polyline points="2,13 7,8 10,11 16,5" fill="none" stroke="#1ad4e8" stroke-width="2"/><polyline points="12,5 16,5 16,9" fill="none" stroke="#1ad4e8" stroke-width="2"/></svg>Trending</div>
<div class="abs side-item caps" style="top:298px">
  <svg viewBox="0 0 18 18"><path d="M9 2 L15 4 V9 C15 13 12 15 9 16 C6 15 3 13 3 9 V4 Z" fill="none" stroke="#999" stroke-width="1.5"/><circle cx="9" cy="9" r="1.5" fill="#999"/></svg>Police</div>
<div class="abs side-item caps" style="top:358px">
  <svg viewBox="0 0 18 18"><path d="M9 2 L17 16 H1 Z" fill="none" stroke="#999" stroke-width="1.5"/><line x1="9" y1="7" x2="9" y2="11" stroke="#999" stroke-width="1.5"/><circle cx="9" cy="13.5" r=".9" fill="#999"/></svg>Chaos</div>
<div class="abs side-item caps" style="top:418px">
  <svg viewBox="0 0 18 18"><path d="M2 3 H8 L5 8 Z M10 3 H16 L13 8 Z" fill="none" stroke="#999" stroke-width="1.5"/><line x1="5" y1="8" x2="5" y2="15" stroke="#999" stroke-width="1.5"/><line x1="13" y1="8" x2="13" y2="15" stroke="#999" stroke-width="1.5"/></svg>Nightlife</div>
<div class="abs side-item caps" style="top:478px">
  <svg viewBox="0 0 18 18"><path d="M4 2 H11 L14 5 V16 H4 Z" fill="none" stroke="#999" stroke-width="1.5"/><path d="M7.5 8 L11 10.5 L7.5 13 Z" fill="#999"/></svg>My Clips</div>
<div class="abs btn-premium caps">Upgrade to Premium</div>

<section class="abs hero" role="img" aria-label="Looping video of a neon-lit Miami beachfront street at dusk with hotels, palm trees and passing cars"></section>
<div class="abs hero-tag caps">Live from the 305</div>
<h1 class="abs hero-title">MIAMI STREETS<span>LIKE NEVER BEFORE</span></h1>
<div class="abs btn-watch">WATCH LIVE NOW</div>
<div class="abs btn-latest">LATEST CHAOS</div>

<section class="abs sponsored caps">
  <small>Sponsored Content</small>
  <strong>Get the Gear // Shift into Overdrive</strong>
</section>

<div class="abs trend-bar"></div>
<h2 class="abs section-title trend-title">TRENDING NOW</h2>
<div class="abs trend-sub caps">Most viral content of the hour</div>
<div class="abs viewers caps"><i></i>4.2K Viewers Live</div>
<div class="abs trend-rule"></div>

<article class="abs feature one" role="img" aria-label="Black and white photo of a police cruiser on a smoky night street">
  <span class="feature-tag caps">Critical Incident</span>
  <h3>HIGH-SPEED PURSUIT ENDS IN WYNWOOD CHAOS</h3>
</article>
<article class="abs feature two" role="img" aria-label="Black and white photo of a crowded street between tall trees">
  <span class="feature-tag caps">Viral Breakout</span>
  <h3>MASSIVE TAKEOVER SHUTS DOWN SOUTH BEACH</h3>
</article>

<h2 class="abs section-title latest-title">LATEST HEAT</h2>
<div class="abs latest-rule"></div>

<div class="abs clip-thumb thumb-crash" style="left:331px;top:1333px" role="img" aria-label="Dented dark car in a studio"></div>
<span class="abs clip-tag pink caps" style="left:347px;top:1347px">Crash</span>
<div class="abs clip-title" style="left:340px;top:1536px">I-95 MULTI-CAR PILEUP CAUGHT ON DASHCAM</div>
<div class="abs clip-meta" style="left:340px;top:1585px">2 HOURS AGO<i></i><span class="views">14.5K VIEWS</span></div>

<div class="abs clip-thumb thumb-street" style="left:540px;top:1333px" role="img" aria-label="City skyline at night reflected in water"></div>
<span class="abs clip-tag cyan caps" style="left:556px;top:1347px">Street</span>
<div class="abs clip-title narrow" style="left:550px;top:1536px">OCEAN DRIVE MELTDOWN: TOTAL CHAOS</div>
<div class="abs clip-meta" style="left:550px;top:1606px">4 HOURS AGO<i></i><span class="views cy">89K VIEWS</span></div>

<div class="abs clip-thumb thumb-night" style="left:331px;top:1652px" role="img" aria-label="Blue neon nightlife sign graphic"></div>
<span class="abs clip-tag pink caps" style="left:347px;top:1666px">Exclusive</span>
<div class="abs clip-title narrow" style="left:349px;top:1855px">UNDERGROUND MEET GONE WRONG IN HIALEAH</div>
<div class="abs clip-meta" style="left:349px;top:1925px;font-size:9px">6 HOURS AGO<i></i><span class="views">22K VIEWS</span></div>

<div class="abs clip-thumb thumb-night" style="left:540px;top:1652px" role="img" aria-label="Blue neon nightlife sign graphic"></div>
<span class="abs clip-tag pink caps" style="left:556px;top:1666px">Exclusive</span>
<div class="abs clip-title narrow" style="left:559px;top:1855px">UNDERGROUND MEET GONE WRONG IN HIALEAH</div>
<div class="abs clip-meta" style="left:559px;top:1925px;font-size:9px">6 HOURS AGO<i></i><span class="views">22K VIEWS</span></div>

<div class="abs btn-more caps">Load More Heat</div>

<aside class="abs topics">
  <h4 class="caps">Hot Topics</h4>
  <span class="hashtag caps" style="left:31px;top:80px">#BrickellChaos</span>
  <span class="hashtag caps" style="left:183px;top:80px">#I95Crashes</span>
  <span class="hashtag caps" style="left:31px;top:124px">#SoBeTakeover</span>
  <span class="hashtag caps" style="left:183px;top:124px">#WynwoodNight</span>
  <span class="hashtag caps" style="left:31px;top:167px">#MiamiPD</span>
</aside>

<aside class="abs ad-box">
  <div class="ad-label caps">Advertisement</div>
  <div class="ad-photo" role="img" aria-label="Fashion photo of a model in a beanie and olive jacket"></div>
  <div class="ad-line caps">Upgrade your rig</div>
  <div class="btn-shop caps">Shop Now</div>
</aside>

<h3 class="abs chatter-title">THE CHATTER</h3>
<div class="abs chatter-rule"></div>
<div class="abs comment cy" style="top:2168px"><b>USER_305_CRASH</b><p>"I was there! That charger almost hit the police cruiser. Crazy scenes."</p></div>
<div class="abs comment pk" style="top:2289px"><b>VICE_CITY_LIFER</b><p>"Brickell is getting out of hand on Friday nights. Needs more patrols."</p></div>

<section class="abs cta">
  <svg class="cta-stripes" width="300" height="346" viewBox="0 0 300 346">
    <polygon points="60,0 100,0 40,346 0,346" fill="#c9748c" opacity=".8"/>
    <polygon points="120,0 160,0 100,346 60,346" fill="#c9748c" opacity=".8"/>
    <polygon points="180,0 220,0 160,346 120,346" fill="#c9748c" opacity=".8"/>
  </svg>
  <h2>GOT THE HEAT?<br>GET PAID.</h2>
  <p>WE PAY COLD CASH FOR YOUR VIRAL MIAMI FOOTAGE.</p>
  <div class="btn-submit-cta">SUBMIT CLIP</div>
</section>
<div class="abs cta-band"></div>

<footer>
  <div class="abs foot-brand"><i></i>TulipaMoonsXo947</div>
  <div class="abs foot-tag caps">Unfiltered Miami Streets Since 2012</div>
  <nav class="abs foot-links caps">
    <span>Terms &amp; Conditions</span><span>Privacy Policy</span><span>DMCA Notice</span><span>Advertising</span><span>Contact Support</span>
  </nav>
  <div class="abs foot-icons">
    <svg viewBox="0 0 24 24"><circle cx="12" cy="12" r="9" fill="none" stroke="#ff8fab" stroke-width="2"/><polyline points="8,12 11,15 16,9" fill="none" stroke="#ff8fab" stroke-width="2"/></svg>
    <svg viewBox="0 0 24 24"><path d="M12 3 C15 8 18 10 18 15 A6 6 0 0 1 6 15 C6 11 9 9 12 3 Z" fill="none" stroke="#ff8fab" stroke-width="2"/><circle cx="12" cy="16" r="2" fill="none" stroke="#ff8fab" stroke-width="2"/></svg>
    <svg viewBox="0 0 24 24"><rect x="3" y="6" width="13" height="12" rx="1" fill="none" stroke="#ff8fab" stroke-width="2"/><polygon points="16,10 21,7 21,17 16,14" fill="none" stroke="#ff8fab" stroke-width="2"/></svg>
  </div>
  <div class="abs legal caps">© 2026 TulipaMoonsXo947. For entertainment purposes only. We do not<br>condone or encourage illegal activities. Stay safe, stay legal.</div>
</footer>

</body>
</html>
```